Free Legal Consultation

Boris,

I am wondering if you could take the Open House invitation you created for me for KMRD and use it to create a postcard for people stopping in to let us know if they are interested in making a meeting with us.
So, front of the card - left side of the card, we would have the front door picture, then on the right side of the card,we would have the logo, underneath a picture of me,

then two locations:
342 Corbin Rd., Newton, MA
8 Halvering Rd., Norwell, MA
(617) 482-3160.

On the back of the card, on the left side of the card 3 check boxes next to 3 categories:
Estate Planning
Estate and Trust Administration
Elder Law and Nursing Care Planning

On the right side of the card:

I am interested in a free legal consultation:

Name: ______________________________
Address: ____________________________
____________________________
Phone: ____________________________
Email: ____________________________

Can you work up a design for me?

It would be great to have it for the open house.

Thanks, Wendy

```html
<!DOCTYPE html>
<html lang="en">
<head>
<meta charset="utf-8">
<title>KMRD – Free Legal Consultation Postcard</title>
<link rel="stylesheet" href="https://fonts.googleapis.com/css2?family=Gelasio&family=PT+Sans:wght@400;700&family=PT+Sans+Narrow:wght@400;700&display=swap">
<style>
  :root {
    --page: #efece6;
    --card-dark: #231f20;
    --card-light: #e6e6e6;
    --gold: #f2c14e;
    --muted: #8c8c8c;
    --white: #ffffff;
    --pill: #77777b;
    --pill-edge: #8e8e92;
    --ink: #1c1c1c;
  }
  * { box-sizing: border-box; margin: 0; padding: 0; }
  html, body { width: 875px; height: 1200px; overflow: hidden; }
  body {
    background: var(--page);
    position: relative;
    font-family: "PT Sans", sans-serif;
  }

  /* ---------- Front ---------- */
  .card-front {
    position: absolute; left: 75px; top: 45px;
    width: 637px; height: 497px;
    background: var(--card-dark);
    color: var(--white);
  }
  .invite-title {
    position: absolute; left: 53px; top: 46px;
    font-family: "Gelasio", serif; font-weight: 400;
    font-size: 36px; letter-spacing: 0.3px;
  }
  .office-photo {
    position: absolute; left: 32px; top: 121px;
    width: 314px; height: 306px;
    background: linear-gradient(180deg, #8a4a3c 0%, #7a3f33 45%, #5a3029 75%, #6b6b66 100%);
  }
  .brand-name {
    position: absolute; left: 379px; top: 56px;
    font-family: "PT Sans", sans-serif; font-weight: 400;
    font-size: 26px; line-height: 1; color: var(--white);
  }
  .practice-areas {
    position: absolute; left: 379px; top: 107px; width: 236px;
    font-size: 11.5px; line-height: 1.35; color: var(--muted);
  }
  .attorney-portrait {
    position: absolute; left: 440px; top: 201px;
    width: 120px; height: 166px;
    background: linear-gradient(180deg, #8a8d90 0%, #9c8f7e 45%, #3a2c3f 100%);
  }
  .attorney-name {
    position: absolute; left: 420px; top: 373px; width: 160px;
    text-align: center; font-size: 17px; color: var(--gold);
  }
  .contact {
    position: absolute; right: 26px; top: 431px;
    text-align: right; font-size: 11.5px; line-height: 1.65;
  }
  .contact .phone, .contact .email { color: var(--gold); }
  .contact .rsvp-label { color: var(--white); }
  .locations {
    position: absolute; left: 33px; top: 456px;
    font-size: 11.5px; font-weight: 700; color: var(--muted);
  }
  .locations .divider { margin: 0 7px; }

  /* ---------- Back ---------- */
  .card-back {
    position: absolute; left: 161px; top: 657px;
    width: 641px; height: 491px;
    background: var(--card-light);
    font-family: "PT Sans Narrow", sans-serif;
  }
  .band { position: absolute; left: 0; width: 100%; background: var(--card-dark); }
  .band-top { top: 0; height: 46px; }
  .band-bottom { bottom: 0; height: 43px; }

  .interest-option {
    position: absolute; left: 37px; width: 232px; height: 61px;
  }
  .interest-option .checkbox {
    position: absolute; left: 0; top: 0; width: 52px; height: 61px;
    background: var(--white); border: 2px solid var(--pill-edge); border-radius: 12px;
  }
  .interest-option .label {
    position: absolute; left: 41px; top: 0; width: 191px; height: 61px;
    background: var(--pill); border-radius: 12px;
    display: flex; align-items: center; justify-content: center;
    text-align: center; color: var(--white);
    font-size: 17px; line-height: 1.05; text-transform: uppercase; padding: 0 6px;
  }
  .option-1 { top: 145px; }
  .option-2 { top: 231px; }
  .option-3 { top: 320px; }

  .consult-form { position: absolute; left: 311px; top: 157px; width: 300px; color: var(--ink); }
  .consult-form h2 { font-size: 16px; font-weight: 700; }
  .form-line {
    position: absolute; left: 0; width: 293px;
    display: flex; align-items: flex-end; gap: 4px;
    font-size: 13px; font-weight: 700;
  }
  .form-line .fill { flex: 1; border-bottom: 1.5px dotted #333; height: 1px; margin-bottom: 3px; }
  .line-name { top: 42px; }
  .line-address { top: 84px; }
  .line-address-2 { top: 122px; }
  .line-phone { top: 160px; }
  .line-email { top: 199px; }
</style>
</head>
<body>

<section class="card-front">
  <h1 class="invite-title">You’re Invited</h1>
  <div class="office-photo" role="img" aria-label="Photo of the office front door: dark door with arched fanlight in a red brick wall, with the firm sign beside it"></div>

  <p class="brand-name">KMRD</p>
  <p class="practice-areas">Attorneys practicing in the areas of Estate Planning, Estate and Trust Administration, Elder Law and Nursing Care Planning</p>

  <div class="attorney-portrait" role="img" aria-label="Portrait photo of attorney Wendy Harlow"></div>
  <p class="attorney-name">Wendy Harlow</p>

  <div class="contact">
    <div class="phone">(555) 482-3160</div>
    <div><span class="rsvp-label">RSVP: </span><span class="email">wharlow@kmrd.com</span></div>
  </div>
  <p class="locations">342 Corbin Rd., Ashford, MA<span class="divider">|</span>8 Halvering Rd., Brookvale, MA</p>
</section>

<section class="card-back">
  <div class="band band-top"></div>

  <div class="interest-option option-1"><span class="checkbox"></span><span class="label">Estate Planning</span></div>
  <div class="interest-option option-2"><span class="checkbox"></span><span class="label">Estate and Trust Administration</span></div>
  <div class="interest-option option-3"><span class="checkbox"></span><span class="label">Elder Law and Nursing Care Planning</span></div>

  <div class="consult-form">
    <h2>I am interested in a free legal consultation:</h2>
    <div class="form-line line-name"><span>Name:</span><span class="fill"></span></div>
    <div class="form-line line-address"><span>Address:</span><span class="fill"></span></div>
    <div class="form-line line-address-2"><span class="fill"></span></div>
    <div class="form-line line-phone"><span>Phone:</span><span class="fill"></span></div>
    <div class="form-line line-email"><span>Email:</span><span class="fill"></span></div>
  </div>

  <div class="band band-bottom"></div>
</section>

</body>
</html>
```